Yorvane crafters

Vesk T620 year 2021 needs a full wrap. My companies name is Yorvane Crafters we are a high end landscape design build company. We specialize in pavers retaining walls, patio covers and decks.

```html
<!DOCTYPE html>
<html lang="en">
<head>
<meta charset="utf-8">
<title>Yorvane Crafters – Truck Wrap</title>
<link href="https://fonts.googleapis.com/css2?family=Marcellus&family=Montserrat:wght@500;700&display=swap" rel="stylesheet">
<style>
  :root{
    --navy-top:#5f6d80;
    --navy-bottom:#2c3d55;
    --wrap-yellow:#f5b822;
    --wrap-white:#f4f4f2;
    --brand-teal:#1f3c4c;
    --rocker:#3d4043;
    --trim:#2a2c2e;
    --glass:#5a6068;
    --tire:#1d1f21;
    --rim:#9a9ea3;
    --chrome:#b9bcc0;
    --tail:#c0242b;
    --head:#e9e9e6;
    --light-bg:#eef1f4;
    --ink:#111111;
  }
  html,body{margin:0;padding:0;overflow:hidden;}
  .canvas{width:1200px;height:1200px;position:relative;overflow:hidden;background:var(--light-bg);}
  .panel-dark{position:absolute;left:0;top:0;width:1200px;height:585px;background:linear-gradient(180deg,var(--navy-top) 0%,var(--navy-top) 65%,var(--navy-bottom) 100%);}
  .divider{position:absolute;left:0;top:585px;width:1200px;height:15px;background:var(--wrap-yellow);}
  .panel-light{position:absolute;left:0;top:600px;width:1200px;height:600px;background:radial-gradient(ellipse at center,#f8f9fb 0%,var(--light-bg) 70%);}
  .brand-lockup{position:absolute;top:48px;right:58px;display:flex;flex-direction:column;align-items:center;color:#fff;}
  .brand-mark{width:34px;height:34px;background:#fff;margin-bottom:8px;}
  .brand-name{font-family:"Marcellus",serif;font-size:16px;letter-spacing:.5px;}
  .brand-tag{font-family:"Montserrat",sans-serif;font-weight:500;font-size:6.5px;letter-spacing:.4px;margin-top:2px;}
  .stage{position:absolute;left:0;top:0;}
  .wrap-name{font-family:"Marcellus",serif;fill:var(--brand-teal);font-size:25px;}
  .wrap-tag{font-family:"Montserrat",sans-serif;font-weight:500;fill:var(--brand-teal);font-size:8.5px;letter-spacing:.5px;}
  .wrap-web{font-family:"Montserrat",sans-serif;font-weight:700;fill:#fff;font-size:10px;}
  .wrap-call{font-family:"Montserrat",sans-serif;font-weight:700;fill:#fff;font-size:10.5px;}
  .wrap-phone{font-family:"Montserrat",sans-serif;font-weight:700;fill:var(--ink);font-size:15px;}
</style>
</head>
<body>
<div class="canvas">
  <div class="panel-dark"></div>
  <div class="divider"></div>
  <div class="panel-light"></div>

  <div class="brand-lockup">
    <div class="brand-mark"></div>
    <div class="brand-name">YORVANE CRAFTERS</div>
    <div class="brand-tag">OUTDOOR LIVING SPACES</div>
  </div>

  <svg class="stage" width="1200" height="1200" viewBox="0 0 1200 1200" xmlns="http://www.w3.org/2000/svg">
    <defs>
      <path id="body-shape" d="M0 90 L190 66 L300 2 L460 2 L466 78 L790 78 L792 165 L685 165 A72 72 0 0 0 565 165 L167 165 A72 72 0 0 0 47 165 L0 165 Z"/>
      <clipPath id="body-clip"><use href="#body-shape"/></clipPath>
      <g id="truck-wrap">
        <ellipse cx="370" cy="262" rx="360" ry="10" fill="#000" opacity=".22"/>
        <rect x="-10" y="128" width="22" height="34" rx="3" fill="var(--chrome)"/>
        <rect x="782" y="132" width="18" height="30" rx="3" fill="var(--chrome)"/>
        <g clip-path="url(#body-clip)">
          <rect x="-5" y="0" width="805" height="180" fill="var(--wrap-white)"/>
          <polygon points="0,0 240,0 180,180 0,180" fill="var(--wrap-yellow)"/>
          <polygon points="255,0 290,0 230,180 195,180" fill="var(--wrap-yellow)"/>
          <polygon points="305,0 328,0 268,180 245,180" fill="var(--wrap-yellow)"/>
          <polygon points="520,78 560,78 520,180 480,180" fill="var(--wrap-yellow)"/>
          <polygon points="575,78 600,78 560,180 535,180" fill="var(--wrap-yellow)"/>
          <polygon points="690,78 800,78 800,180 640,180" fill="var(--wrap-yellow)"/>
          <polygon points="720,78 745,78 705,180 680,180" fill="var(--wrap-white)"/>
          <rect x="-5" y="145" width="810" height="40" fill="var(--rocker)"/>
          <line x1="466" y1="78" x2="466" y2="145" stroke="var(--trim)" stroke-width="2"/>
          <line x1="350" y1="10" x2="350" y2="145" stroke="var(--trim)" stroke-width="1.5" opacity=".5"/>
        </g>
        <path d="M52 165 A67 67 0 0 1 162 165" fill="none" stroke="var(--trim)" stroke-width="9"/>
        <path d="M570 165 A67 67 0 0 1 680 165" fill="none" stroke="var(--trim)" stroke-width="9"/>
        <polygon points="196,72 300,12 344,12 344,72" fill="var(--glass)"/>
        <polygon points="356,12 452,12 454,72 356,72" fill="var(--glass)"/>
        <rect x="2" y="94" width="10" height="30" rx="3" fill="var(--head)"/>
        <rect x="778" y="84" width="12" height="40" rx="2" fill="var(--tail)"/>
        <circle cx="107" cy="205" r="55" fill="var(--tire)"/>
        <circle cx="625" cy="205" r="55" fill="var(--tire)"/>
        <circle cx="107" cy="205" r="36" fill="var(--rim)"/>
        <circle cx="625" cy="205" r="36" fill="var(--rim)"/>
        <circle cx="107" cy="205" r="10" fill="var(--tire)"/>
        <circle cx="625" cy="205" r="10" fill="var(--tire)"/>
      </g>
    </defs>

    <g class="truck truck-driver">
      <use href="#truck-wrap" transform="translate(207 200)"/>
      <text class="wrap-web" x="262" y="302">yorvanecrafters.com</text>
      <rect x="435" y="282" width="40" height="40" fill="var(--brand-teal)"/>
      <text class="wrap-name" x="486" y="298">YORVANE</text>
      <text class="wrap-name" x="486" y="322">CRAFTERS</text>
      <text class="wrap-tag" x="540" y="336">OUTDOOR LIVING SPACES</text>
      <polygon points="703,288 822,288 812,307 703,307" fill="var(--ink)"/>
      <text class="wrap-call" x="716" y="301">Call Us Now!</text>
      <text class="wrap-phone" x="826" y="303">(555) 014-2873</text>
    </g>

    <g class="truck truck-passenger">
      <use href="#truck-wrap" transform="translate(994 766) scale(-1 1)"/>
      <polygon points="223,853 350,853 340,872 223,872" fill="var(--ink)"/>
      <text class="wrap-call" x="238" y="866">Call Us Now!</text>
      <text class="wrap-phone" x="365" y="868">(555) 014-2873</text>
      <text class="wrap-name" x="534" y="866">YORVANE</text>
      <text class="wrap-name" x="534" y="890">CRAFTERS</text>
      <text class="wrap-tag" x="534" y="903">OUTDOOR LIVING SPACES</text>
      <rect x="708" y="852" width="40" height="40" fill="var(--brand-teal)"/>
      <text class="wrap-web" x="828" y="867">yorvanecrafters.com</text>
    </g>
  </svg>
</div>
</body>
</html>
```